Brimvale Crest Homes needs a business card

We need a business card for a new company in Canada, Ontario. Our company is all about luxury contraction homes for our clients. Our product and services are custom projects design. Under the business logo that will be created, we want a slogan that will be a memorable phrase for consumers to remember us to tell their friends and relatives.

Additional infomation
- Teodoro Vanlesky
- President / Ceo
-519.304.7718

Find point what luxury construction products and services can be done

We like to see colors:
- #663300
- and something other colors or color that would attract the client needs and wants

The final design should communicate leads from new or old clients that will grow our empire. Most of all, we try to work among the budget that clients want

NOTE
- we also need an icon for the business (Example: Instagram, Facebook, and Whatsapp icons)
- We want the company name to be remembered easily for clients and our distributors who would get our orders.
- we need an icon on the business cards: Facebook and Instagram.

Thanks,
Brimvale Crest Homes

```html
<!DOCTYPE html>
<html lang="en">
<head>
<meta charset="utf-8">
<title>Brimvale Crest Homes – Business Card</title>
<link rel="stylesheet" href="https://fonts.googleapis.com/css2?family=Open+Sans:wght@400;600;800&display=swap">
<style>
  :root {
    --backdrop: #2b2b2c;
    --card: #1c1c1d;
    --brown: #6b3a12;
    --brown-text: #7a4317;
    --white: #f2f2f2;
    --divider: #4a4a4a;
  }
  * { box-sizing: border-box; margin: 0; padding: 0; }
  html, body {
    width: 1200px; height: 895px; overflow: hidden;
    background: var(--backdrop);
    font-family: "Open Sans", sans-serif;
  }
  .stage {
    width: 1200px; height: 895px;
    display: flex; flex-direction: column; align-items: center; justify-content: center;
    gap: 40px;
  }
  .card {
    position: relative;
    width: 600px; height: 343px;
    background: var(--card);
    box-shadow: 0 10px 30px rgba(0,0,0,.45);
    overflow: hidden;
  }
  .brand {
    position: absolute; left: 0; right: 0;
    text-align: center; color: var(--brown-text);
  }
  .brand-name {
    font-weight: 800; font-size: 40px; letter-spacing: -0.5px; line-height: 1;
  }
  .brand-tagline {
    margin-top: 6px; font-weight: 600; font-size: 13px; letter-spacing: 0.3px;
  }
  .card-front .brand { top: 135px; }
  .card-back .brand { top: 72px; }
  .card-back .brand-name { font-size: 36px; }
  .card-back .brand-tagline { font-size: 12px; }

  .person {
    position: absolute; right: 318px; top: 178px; text-align: right;
  }
  .person-name {
    color: var(--brown-text); font-weight: 600; font-size: 19px; letter-spacing: 0.5px;
  }
  .person-title {
    color: var(--white); font-size: 13px; margin-top: 2px;
  }
  .divider {
    position: absolute; left: 300px; top: 160px; width: 1px; height: 80px;
    background: var(--divider);
  }
  .contacts {
    position: absolute; left: 318px; top: 164px; list-style: none;
  }
  .contacts li {
    display: flex; align-items: center; gap: 9px;
    color: var(--white); font-size: 12.5px; line-height: 24px;
  }
  .contacts svg { width: 12px; height: 12px; fill: var(--brown-text); flex: none; }
  .address-band {
    position: absolute; left: 0; right: 0; bottom: 0; height: 38px;
    background: var(--brown);
    color: var(--white); font-size: 13px; letter-spacing: 0.3px;
    display: flex; align-items: center; justify-content: center;
  }
</style>
</head>
<body>
<main class="stage">
  <section class="card card-front">
    <div class="brand">
      <div class="brand-name">Brimvale Crest Homes</div>
      <div class="brand-tagline">- HOME RENOVATIONS - CUSTOM PROJECT DESIGN -</div>
    </div>
  </section>

  <section class="card card-back">
    <div class="brand">
      <div class="brand-name">Brimvale Crest Homes</div>
      <div class="brand-tagline">- HOME RENOVATIONS - CUSTOM PROJECT DESIGN -</div>
    </div>
    <div class="person">
      <div class="person-name">TEODORO VANLESKY</div>
      <div class="person-title">President / CEO</div>
    </div>
    <div class="divider"></div>
    <ul class="contacts">
      <li>
        <svg viewBox="0 0 24 24" aria-hidden="true"><path d="M6.6 10.8a15.1 15.1 0 0 0 6.6 6.6l2.2-2.2c.3-.3.7-.4 1-.2 1.1.4 2.3.6 3.6.6.6 0 1 .4 1 1V20c0 .6-.4 1-1 1A17 17 0 0 1 3 4c0-.6.4-1 1-1h3.5c.6 0 1 .4 1 1 0 1.3.2 2.5.6 3.6.1.3 0 .7-.2 1z"/></svg>
        519.304.7718
      </li>
      <li>
        <svg viewBox="0 0 24 24" aria-hidden="true"><path d="M2 5h20v14H2z M2 5l10 8 10-8" fill="none" stroke="#7a4317" stroke-width="2"/><path d="M2 5h20l-10 8z"/></svg>
        info@brimvalecresthomes.com
      </li>
      <li>
        <svg viewBox="0 0 24 24" aria-hidden="true"><circle cx="12" cy="12" r="10"/><path d="M2 12h20M12 2c3 3 3 17 0 20M12 2c-3 3-3 17 0 20" fill="none" stroke="#1c1c1d" stroke-width="1.5"/></svg>
        www.brimvalecresthomes.com
      </li>
    </ul>
    <div class="address-band">2840 Harlow Ridge Rd. #210, Oakmere, ON L4B 7K2</div>
  </section>
</main>
</body>
</html>
```